Career Counselor in need of a business card design

Hello Creatives! I'm in need of a business card design for a new company based in Georgia, USA called Pathways By Lantern.

Some things that may be helpful in creating your concept(s) include:

My Logo (Included in the Files section): There are three versions, two versions are in the second file. The all gold stacked (vertical) version is my primary logo and then there are two horizontal versions (one is all gold and the other is gold and grey).

My mission: to empower tweens through young adults to realize and actualize their CAREER ASPIRATIONS.
My vision: for tweens through young adults to LIVE LIFE ON PURPOSE and become CONTRIBUTING MEMBERS OF SOCIETY.

Biblical scriptures that support my ‘Why’: Psalms 127: 3-4(NIV) Children are a heritage from the Lord, offspring a reward from him. Like ARROWS in the hands of a warrior are children…. And Proverbs 29:18(JKV) Where there is no VISION, the people perish.

*Words in ALL CAPS are to emphasize what's important to me and may possibly provide you some inspiration (IDK - Have fun with it)!

Target Market(s)

My ideal customers are parents, guardians, and young adults.

Contact Information for Business Card

My name, degrees and credential: Delphine Marlow, M.S., Ed.S., NCC
Title: College and Career Coach and Consultant

Number: 555.318.2907
Address: 2718 Willowmere Avenue., Suite 405, Macon, GA 31299
Email: info@pathwaysbylantern.example
Website: www.pathwaysbylantern.example

My population: TWEENS • TEENS • EMERGING ADULTS
Services offered: One-On-One Sessions • Small Groups • Workshops

Colors

Designer to choose colors to be used in the design.

Requirements
Nice to have
• Either my mission or vision but I will understand if it does not all fit.
• My mission: To empower tweens through young adults to realize and actualize their career aspirations.
• My vision: For tweens through young adults to live life on purpose and become contributing members of society.

```html
<!DOCTYPE html>
<html lang="en">
<head>
<meta charset="utf-8">
<title>Pathways By Lantern — Business Card</title>
<link rel="stylesheet" href="https://fonts.googleapis.com/css2?family=Cinzel:wght@400;600&family=Tinos:wght@700&family=Titillium+Web:wght@400;600&display=swap">
<style>
  :root {
    --backdrop: #2a2a2c;
    --card-dark: #0e0e0f;
    --card-light: #ffffff;
    --gold: #c99a2e;
    --gold-soft: rgba(201, 154, 46, 0.14);
    --gold-faint: rgba(201, 154, 46, 0.18);
    --text-grey: #9a9a9a;
    --text-dark: #3c3c3c;
  }
  * { box-sizing: border-box; margin: 0; padding: 0; }
  html, body { width: 1200px; height: 900px; overflow: hidden; }
  body {
    background: var(--backdrop);
    font-family: "Titillium Web", sans-serif;
    position: relative;
  }
  .card {
    position: absolute;
    left: 280px;
    width: 640px;
    height: 366px;
    overflow: hidden;
    box-shadow: 0 14px 30px rgba(0,0,0,0.45);
  }
  .card--back { top: 66px; background: var(--card-dark); }
  .card--front { top: 468px; background: var(--card-light); }

  .brand {
    position: absolute;
    display: flex;
    align-items: center;
    gap: 14px;
  }
  .brand__dot {
    width: 54px; height: 54px;
    border-radius: 50%;
    border: 3px solid var(--gold);
    flex: none;
  }
  .brand__name {
    font-family: "Cinzel", serif;
    font-weight: 600;
    color: var(--gold);
    line-height: 1.05;
    letter-spacing: 1px;
  }
  .card--back .brand { left: 36px; top: 28px; }
  .card--back .brand__name { font-size: 26px; }
  .card--front .brand { left: 40px; top: 112px; }
  .card--front .brand__dot { width: 82px; height: 82px; }
  .card--front .brand__name {
    font-size: 32px;
    padding-left: 18px;
    border-left: 2px solid var(--gold);
  }

  .decor-ring {
    position: absolute;
    border-radius: 50%;
  }
  .card--back .decor-ring {
    width: 300px; height: 300px;
    right: 10px; top: 52px;
    border: 14px solid var(--gold-soft);
  }
  .card--front .decor-ring {
    width: 320px; height: 320px;
    right: 20px; top: 130px;
    border: 16px solid var(--gold-faint);
  }

  .audience {
    position: absolute;
    left: 40px; top: 116px;
    font-size: 15px;
    letter-spacing: 0.5px;
    color: var(--text-grey);
  }
  .bullet { color: var(--gold); margin: 0 5px; }

  .services {
    position: absolute;
    left: 36px; top: 186px;
  }
  .services__title {
    font-family: "Cinzel", serif;
    font-size: 21px;
    color: var(--text-grey);
    letter-spacing: 1px;
    padding: 4px 60px 2px 2px;
    border-top: 2px solid var(--gold);
    border-bottom: 2px solid var(--gold);
    display: inline-block;
  }
  .services__list {
    margin-top: 12px;
    font-size: 16px;
    color: var(--text-grey);
  }

  .person {
    position: absolute;
    right: 34px; top: 34px;
    text-align: right;
  }
  .person__name {
    font-family: "Tinos", serif;
    font-weight: 700;
    font-size: 24px;
    color: var(--gold);
  }
  .person__title {
    font-size: 17px;
    color: var(--text-dark);
    margin-top: 2px;
  }

  .contact {
    position: absolute;
    left: 210px; top: 248px;
    padding-left: 14px;
    border-left: 2px solid var(--gold);
    font-size: 16px;
    color: var(--text-dark);
    line-height: 24px;
  }
  .contact__row { display: flex; align-items: center; gap: 10px; }
  .contact__row svg { width: 15px; height: 15px; flex: none; }
  .address {
    position: absolute;
    left: 210px; top: 328px;
    font-size: 16px;
    color: var(--text-dark);
  }
</style>
</head>
<body>
  <section class="card card--back" aria-label="Card back">
    <div class="decor-ring"></div>
    <div class="brand">
      <span class="brand__dot"></span>
      <span class="brand__name">Pathways By Lantern</span>
    </div>
    <p class="audience">TWEENS<span class="bullet">•</span>TEENS<span class="bullet">•</span>EMERGING ADULTS</p>
    <div class="services">
      <h2 class="services__title">SERVICES OFFERED</h2>
      <p class="services__list">One-On-One Sessions<span class="bullet">•</span>Small Groups<span class="bullet">•</span>Workshops</p>
    </div>
  </section>

  <section class="card card--front" aria-label="Card front">
    <div class="decor-ring"></div>
    <div class="person">
      <h1 class="person__name">Delphine Marlow, M.S., Ed.S., NCC</h1>
      <p class="person__title">College and Career Coach and Consultant</p>
    </div>
    <div class="brand">
      <span class="brand__dot"></span>
      <span class="brand__name">Pathways<br>By Lantern</span>
    </div>
    <div class="contact">
      <div class="contact__row">
        <svg viewBox="0 0 16 16" fill="#c99a2e"><path d="M3 1h3l1.5 4-2 1.3a9 9 0 0 0 4.2 4.2L11 8.5l4 1.5v3a2 2 0 0 1-2 2A12 12 0 0 1 1 3a2 2 0 0 1 2-2z"/></svg>
        <span>555.318.2907</span>
      </div>
      <div class="contact__row">
        <svg viewBox="0 0 16 16" fill="none" stroke="#c99a2e" stroke-width="1.6"><rect x="1" y="3" width="14" height="10"/><path d="M1 3l7 6 7-6"/></svg>
        <span>info@pathwaysbylantern.example</span>
      </div>
      <div class="contact__row">
        <svg viewBox="0 0 16 16" fill="none" stroke="#c99a2e" stroke-width="1.4"><circle cx="8" cy="8" r="6.5"/><ellipse cx="8" cy="8" rx="3" ry="6.5"/><path d="M1.5 8h13"/></svg>
        <span>www.pathwaysbylantern.example</span>
      </div>
    </div>
    <p class="address">2718 Willowmere Avenue., Suite 405, Macon, GA 31299</p>
  </section>
</body>
</html>
```